Brovanta Healthcare Services ( a Communitiy Mental Health Services with a full continuum of services

Our company colors are esspresso brown and french vanilla. Our message is "Your partner in Healthcare" This is the individual client's partner and other community agencies' partner. Some fresh green to express new growth or new beginnings or healing could be used - as well as other colors as long as the main colors are company colors.
We provide Outpatient Treatment for mental health and substance abuse disorders. We also have a Crisis continuum that includes a Walk-In assessment center, Mobile Crisis, Crisis Stabilazation, Medically Monitored Detox and Respite.
We have been in business over 30 years and want to send the message of being a solid, forward thinking, cutting edge, provider who focuses on quality and evidenced based treatment.
The attachment includes our logo that must be used. The wording only includes the Crisis continuum - except the part that describes the company on the back page.

Healthcare

```html
<!DOCTYPE html>
<html lang="en">
<head>
<meta charset="UTF-8">
<title>Brovanta Healthcare Services – Crisis Continuum Brochure</title>
<link rel="stylesheet" href="https://fonts.googleapis.com/css2?family=Montserrat:wght@400;500&family=Oswald:wght@400&display=swap">
<style>
  :root {
    --backdrop: #e6e6e6;
    --vanilla-light: #fbe9b2;
    --vanilla: #f5d98c;
    --vanilla-deep: #eecd77;
    --espresso: #4b3220;
    --espresso-dark: #2f1f13;
    --ink: #2c2116;
    --cream-text: #f2d48a;
  }
  * { box-sizing: border-box; margin: 0; padding: 0; }
  html, body { width: 1200px; height: 800px; overflow: hidden; }
  body {
    background: var(--backdrop);
    display: flex;
    align-items: center;
    justify-content: center;
    font-family: "Montserrat", Arial, sans-serif;
  }
  .brochure {
    display: flex;
    width: 1140px;
    height: 740px;
    box-shadow: 0 10px 30px rgba(0,0,0,0.18);
  }
  .panel {
    flex: 1;
    min-width: 0;
    padding: 36px 30px 30px;
    font-size: 11.5px;
    line-height: 1.4;
    color: var(--ink);
  }
  .panel--vanilla {
    background: linear-gradient(160deg, var(--vanilla-light), var(--vanilla) 60%, var(--vanilla-deep));
  }
  .panel--espresso {
    background: linear-gradient(170deg, var(--espresso), var(--espresso-dark));
    color: var(--cream-text);
  }
  .service-title {
    font-size: 13px;
    font-weight: 500;
    text-transform: uppercase;
    letter-spacing: 0.04em;
    text-align: center;
    margin-bottom: 12px;
    line-height: 1.3;
  }
  .section-label {
    font-size: 12px;
    font-weight: 500;
    text-transform: uppercase;
    letter-spacing: 0.03em;
    margin: 14px 0 7px;
  }
  .panel p { margin-bottom: 9px; }
  .panel p:last-child { margin-bottom: 0; }
  .panel p.justify { text-align: justify; }
  .headline {
    font-family: "Oswald", "Arial Narrow", sans-serif;
    font-weight: 400;
    text-transform: uppercase;
    text-align: center;
    font-size: 40px;
    line-height: 1.0;
    letter-spacing: 0.02em;
    padding: 10px 0 12px;
    margin-bottom: 18px;
    border-top: 2px solid var(--cream-text);
    border-bottom: 2px solid var(--cream-text);
  }
  .headline .line-sm { font-size: 34px; display: block; }
  .service-gap { margin-top: 20px; }
</style>
</head>
<body>
  <main class="brochure">
    <section class="panel panel--vanilla">
      <h2 class="service-title">Crisis Assessment Center<br>(CAC) &amp; Mobile Crisis</h2>
      <h3 class="section-label">Who do we serve?</h3>
      <p class="justify">Individuals who walk-in, or are brought in by police and individuals in the community at local hospitals, physician offices, outpatient clinics, individual homes, and other community settings where a person is experiencing an emotional/behavioral health crisis.</p>
      <h3 class="section-label">Program Description</h3>
      <p>BHS's goal is to provide crisis de-escalation services, referral to least restrictive appropriate level of care.</p>
      <p>Focus on interventions and resources which will aid in stabilizing the individual.</p>
      <p>Link the individual to the least restrictive level of care determined be appropriate.</p>
      <p class="justify">Referrals include: inpatient psychiatric hospital resources, intensive outpatient treatment, case management, outpatient therapy (individual, family and group) and psychiatric evaluation/medication as indicated by the needs of the individual.</p>
    </section>

    <section class="panel panel--espresso">
      <h1 class="headline">Over 30<br><span class="line-sm">Years of</span><span class="line-sm">Experience</span></h1>
      <h2 class="service-title">Crisis Stabilization<br>Unit (CSU)</h2>
      <h3 class="section-label">Who do we serve?</h3>
      <p class="justify">TN residents age 18 and older who have StateCare or are uninsured and are experiencing an emotional/behavioral health crisis.</p>
      <h3 class="section-label">Program Description</h3>
      <p class="justify">Medication evaluation and management, therapeutic and educational groups, individual therapy, family therapy.</p>
      <p class="justify">Focused toward building on the individual's strengths and building the skills needed to help cope with future stressors, avoid relapse, and promote recovery in future.</p>
      <p class="justify">Education on importance of taking medication and keeping scheduled follow-up appointments with a local community mental health provider.</p>
      <p>Link that individual to the provider of choice.</p>
    </section>

    <section class="panel panel--vanilla">
      <h2 class="service-title">Crisis Respite</h2>
      <h3 class="section-label">Who do we serve?</h3>
      <p>TN residents age 18 and older who are experiencing a mental health crisis and need a brief period of rest and support out of their natural environment.</p>
      <h3 class="section-label">Program Description</h3>
      <p>Peer specialists are available to provide support and companionship to individuals who may otherwise not be able to stay on their own during a mental health crisis.</p>
      <h2 class="service-title service-gap">Medically Monitored<br>Crisis Detox</h2>
      <h3 class="section-label">Who do we serve?</h3>
      <p>TN residents age 18 and older who are uninsured or have BridgeCare and who are in crisis and intoxicated or experiencing the adverse effects of withdrawal from alcohol or other drugs.</p>
      <h3 class="section-label">Program Description</h3>
      <p>National Society of Recovery Medicine (NSRM) level III-7D medically monitored detoxification center.</p>
      <p>Licensed, certified or registered clinicians provide 24-hour care and treatment.</p>
      <p class="justify">An interdisciplinary team provides medical services, individual and group therapy, withdrawal support, and referral to appropriate outpatient follow-up services.</p>
    </section>
  </main>
</body>
</html>
```